Bref créative |
Personal Chef Website Design | ||
New Website | ||
Chef / Catering | ||
www.lenasharvesttable.com | ||
Lena's Harvest Table prepares fresh, ready-to-cook gourmet dinners for on-the-go families with twice a week home delivery. All dinners are prepared weekly with fresh ingredients using the same care and passion Lena uses to prepare dinners for her own family. | ||
See creative brief uploaded as separate doc. Typically like bright, vibrant colors. The most influential colors in terms of food are: red, orange, yellow. An easy to read and use site is important to us |
Clean/Simple Friendly Family Oriented Colorful Service Oriented Feminine |
top | ||
www.fitplatehub.com | ||
www.suppernest.com | ||
facebook.com/lenasharvesttable | ||
See separate creative brief doc, logo and images for use in designing the site. If you have any questions or need further clarity on anything, don't hesitate to ask. | ||

```html
<!DOCTYPE html>
<html lang="en">
<head>
<meta charset="utf-8">
<title>Lena's Harvest Table</title>
<link href="https://fonts.googleapis.com/css2?family=Open+Sans:wght@400;600;700&family=Lora:wght@700&display=swap" rel="stylesheet">
<style>
:root{
  --green:#5f9418;
  --green-dark:#3f6b0c;
  --orange:#ef8a17;
  --red:#d8302a;
  --cream:#f6efdc;
  --stripe:#efe4c8;
  --ink:#444;
  --muted:#888;
  --line:#dcd4bf;
  --white:#fff;
}
*{margin:0;padding:0;box-sizing:border-box}
html,body{width:1200px;height:1062px;overflow:hidden}
body{font-family:"Open Sans",Arial,sans-serif;color:var(--ink);font-size:9px;line-height:1.35;
  background:repeating-linear-gradient(90deg,var(--cream) 0 18px,var(--stripe) 18px 36px);position:relative}
.abs{position:absolute}
.page{position:absolute;left:232px;top:0;width:740px;height:1062px}
/* header */
.header{left:0;top:0;width:740px;height:73px;background:linear-gradient(#fbf6e8,#fff)}
.utility{right:6px;top:3px;font-size:7px;color:var(--muted)}
.utility span{margin-left:6px}
.nav{font-weight:700;color:var(--green);font-size:11px;line-height:1.1}
.nav a{position:absolute;text-decoration:none;color:inherit;text-align:center}
.navbar{left:0;top:66px;width:740px;height:4px;background:var(--green)}
.logo{left:270px;top:4px;width:200px;height:66px;background:var(--white);border-radius:0 0 12px 12px;text-align:center}
.logo .mark{width:30px;height:30px;border-radius:50%;background:var(--green);margin:6px auto 2px}
.logo .name{font-family:"Lora",Georgia,serif;font-weight:700;color:var(--red);font-size:15px}
/* hero */
.hero{left:0;top:73px;width:740px;height:234px;background:linear-gradient(120deg,#e7c08f,#f5e2c4 45%,#c98e5a)}
.caption{left:0;top:190px;width:300px;height:34px;background:rgba(255,255,255,.85);padding:4px 10px}
.caption b{color:var(--red);font-size:11px;display:block}
.dots{right:16px;top:212px}
.dots i{display:inline-block;width:8px;height:8px;border-radius:50%;background:#fff;margin-left:4px;opacity:.7}
.dots i:first-child{opacity:1;background:var(--orange)}
/* promos */
.promo{top:312px;width:244px;height:96px;background:var(--white);border:1px solid var(--line);padding:6px 8px}
.promo .pic{position:absolute;right:6px;top:10px;width:90px;height:74px;border-radius:4px}
.promo small{font-size:7px;display:block;color:var(--muted)}
.promo .big{font-size:30px;font-weight:700;line-height:1}
/* sections */
.title{font-weight:700;font-size:11px;color:var(--green-dark);border-bottom:1px solid var(--line);padding-bottom:2px;margin-bottom:6px}
.title em{float:right;font-style:normal;font-weight:400;font-size:7px;color:var(--muted)}
.box{background:var(--white);border:1px solid var(--line);padding:6px}
.menu-card{position:absolute;top:22px;width:160px;height:165px;border:1px solid var(--line);background:var(--white)}
.menu-card h4{font-size:8px;padding:3px 5px}
.menu-card .pic{height:60px;background:linear-gradient(#d48b3e,#f2c988)}
.menu-card .seal{position:absolute;right:6px;top:48px;width:36px;height:36px;border-radius:50%}
.menu-card ul{list-style:none;padding:5px;font-size:7px}
.menu-card li{margin-bottom:2px}
.menu-card li:before{content:"✓ ";color:var(--green)}
.btn{display:inline-block;background:var(--green);color:#fff;font-weight:700;font-size:8px;padding:3px 8px;border-radius:2px}
.side-head{color:#fff;font-weight:700;font-size:10px;padding:3px 6px}
.field{font-size:7px;color:var(--muted);margin-top:6px}
.field div{height:16px;border:1px solid var(--line);background:#fff;margin-top:2px}
/* footer */
.footer{left:0;top:899px;width:1200px;height:126px;background:#f3ede0;border-top:3px solid var(--green)}
.fcol{top:10px;width:220px}
.fcol h5{font-size:11px;color:var(--green-dark);margin-bottom:5px}
.fcol li{list-style:none;font-size:7.5px;color:var(--muted);margin-bottom:3px}
.fcol li:before{content:"› ";color:var(--orange)}
.social li:before{content:none}
.social i{display:inline-block;width:10px;height:10px;background:var(--green);vertical-align:middle;margin-right:5px}
.bottom{left:0;top:1025px;width:1200px;height:37px;background:#fff}
</style>
</head>
<body>
<div class="page">
  <div class="abs header"></div>
  <div class="abs utility"><span>Pay Online</span><span>My Account</span><span>FAQ</span><span>Contact</span></div>
  <nav class="abs nav" style="left:0;top:0;width:740px;height:73px">
    <a style="left:18px;top:40px">Home</a>
    <a style="left:70px;top:40px">How it Works</a>
    <a style="left:160px;top:40px">The Kitchen</a>
    <a style="left:480px;top:34px">Our Current<br>Menu</a>
    <a style="left:565px;top:34px">Catering<br>Services</a>
    <a style="left:640px;top:34px">Lena's<br>Passion</a>
  </nav>
  <div class="abs navbar"></div>
  <div class="abs logo"><div class="mark"></div><div class="name">Lena's Harvest Table</div></div>

  <div class="abs hero" role="img" aria-label="Smiling family sharing a home-cooked dinner at the table"></div>
  <div class="abs caption" style="top:263px"><b>No More Worrying About What's For Dinner Tonight</b><span style="font-size:7px">Fresh gourmet meals delivered to your door twice a week</span></div>
  <div class="abs dots" style="top:288px"><i></i><i></i><i></i><i></i></div>

  <div class="abs promo" style="left:0"><small>Get Your Dinner</small><div class="big" style="color:var(--green)">Free</div><small>with your first order<br>Invite a friend and your<br>next dinner is on us</small>
    <div class="pic" role="img" aria-label="Plated dinner" style="background:linear-gradient(#b9d58a,#e6b46b)"></div></div>
  <div class="abs promo" style="left:248px"><small>Sign Up Today</small><div class="big" style="color:var(--orange)">$0.00</div><small>delivery fee<br>on all home orders<br>this month only</small>
    <div class="pic" role="img" aria-label="Fresh pasta dish" style="background:linear-gradient(#f0c06a,#c9743a)"></div></div>
  <div class="abs promo" style="left:496px"><small>Ordering is</small><div class="big" style="color:var(--red)">Free</div><small>no contracts, no hidden<br>fees, cancel anytime</small>
    <div class="pic" role="img" aria-label="Salad bowl" style="background:linear-gradient(#c6dc8c,#d8583a)"></div></div>

  <!-- how it works -->
  <section class="abs" style="left:0;top:425px;width:513px">
    <div class="title">How it works <em>» view all</em></div>
    <div class="abs" role="img" aria-label="Gourmet dishes on a counter" style="left:0;top:22px;width:120px;height:120px;background:linear-gradient(135deg,#e8a45a,#8c5a2e)"></div>
    <div class="abs" style="left:130px;top:22px;width:380px;font-size:7.5px">
      <p>Lena's Harvest Table prepares fresh, ready-to-cook gourmet dinners for on-the-go families with twice a week home delivery. All dinners are prepared weekly with fresh ingredients using the same care and passion Lena uses to prepare dinners for her own family.</p>
      <p style="margin-top:6px;font-weight:700;color:var(--green-dark)">Getting started is easy:</p>
      <p>1) Log on to www.lenasharvesttable.com<br>2) Look through our gourmet dinner menu. We have a fresh dinner menu that we update every week. We feature a dinner each day of the week and you can see what we're planning to make over the next 4 weeks.</p>
    </div>
  </section>

  <!-- menu -->
  <section class="abs" style="left:0;top:590px;width:513px;height:200px">
    <div class="title">Our current menu <em>» view all</em></div>
    <div class="menu-card" style="left:0"><h4>Basic · 4 Weeks</h4><div class="pic" role="img" aria-label="Pizza"></div><div class="seal" style="background:var(--green)"></div>
      <ul><li>Advantage no. 1</li><li>Advantage no. 2</li><li>Advantage no. 3</li><li>Advantage no. 4</li><li>Advantage no. 5</li></ul></div>
    <div class="menu-card" style="left:176px"><h4>Premium · 4 Weeks</h4><div class="pic" role="img" aria-label="Pizza"></div><div class="seal" style="background:#3a8ccf"></div>
      <ul><li>Advantage no. 1</li><li>Advantage no. 2</li><li>Advantage no. 3</li><li>Advantage no. 4</li><li>Advantage no. 5</li></ul></div>
    <div class="menu-card" style="left:352px"><h4>Platinum · 4 Weeks</h4><div class="pic" role="img" aria-label="Pizza"></div><div class="seal" style="background:var(--orange)"></div>
      <ul><li>Advantage no. 1</li><li>Advantage no. 2</li><li>Advantage no. 3</li><li>Advantage no. 4</li><li>Advantage no. 5</li></ul></div>
  </section>

  <section class="abs" style="left:0;top:795px;width:250px;font-size:7.5px">
    <div class="title">Lena's Passion <em>» view all</em></div>
    <p>Lena was born and raised in Chicago. Her family emigrated to the United States bringing recipes that Americans came to love. Growing up, Lena was always encouraged to spend time with her mother and father sharing their passion for cooking with her. Dinner at her parents' home ...</p>
  </section>
  <section class="abs" style="left:262px;top:795px;width:251px;font-size:7.5px">
    <div class="title">Testimonials <em>» view all</em></div>
    <p>"Delicious!!!"<br>"Happiest weeknight dinner I've ever enjoyed"<br>"My whole family enjoyed every bit of it"<br>"The food was wonderful"<br>"The lasagna was very very good"</p>
  </section>

  <!-- sidebar -->
  <aside class="abs" style="left:523px;top:425px;width:217px">
    <div class="side-head" style="background:var(--green)">Search the Kitchen</div>
    <div class="box" style="height:30px;position:relative"><div style="position:absolute;left:6px;top:7px;width:140px;height:15px;border:1px solid var(--line)"></div><span class="btn" style="position:absolute;right:6px;top:7px">Search</span></div>
    <div class="side-head" style="background:var(--orange);margin-top:4px">Weight Calculator</div>
    <div class="box" style="font-size:7px;height:86px">
      <p>Systems: ○ Metric &nbsp;● Imperial</p>
      <p style="margin-top:5px">Weight: ___ KG &nbsp; Height: ___ CM</p>
      <p style="margin-top:5px">Gender: ___ &nbsp; Age: ___</p>
      <span class="btn" style="margin-top:8px;background:var(--orange)">Calculate</span>
    </div>
    <div class="side-head" style="background:var(--green-dark);margin-top:4px">Get in Touch</div>
    <div class="box" style="height:210px">
      <div class="field">Enter your name<div></div></div>
      <div class="field">Enter your email<div></div></div>
      <div class="field">Enter your phone number<div></div></div>
      <div class="field">Enter your question<div style="height:60px"></div></div>
      <span class="btn" style="float:right;margin-top:5px">Send</span>
    </div>
  </aside>
</div>

<footer class="abs footer">
  <div class="abs fcol" style="left:252px"><h5>Best Services</h5><ul><li>How it Works</li><li>Our Current Menu</li><li>The Kitchen</li><li>Catering Services</li><li>Lena's Passion</li></ul></div>
  <div class="abs fcol" style="left:500px"><h5>Frequently Asked Questions</h5><ul><li>How often do you deliver?</li><li>Does someone have to be at home to accept delivery?</li><li>What is your delivery area?</li><li>Why do I have to order in advance?</li><li>How many meals a week do you deliver?</li></ul></div>
  <div class="abs fcol social" style="left:790px;width:180px"><h5>Find us on:</h5><ul><li><i></i>Join our page</li><li><i></i>Follow our feed</li><li><i></i>Watch our videos</li><li><i></i>Read our blog</li></ul></div>
</footer>
<div class="abs bottom">
  <div class="abs" style="left:242px;top:10px;font-family:'Lora',Georgia,serif;font-weight:700;color:var(--red);font-size:13px">Lena's Harvest Table</div>
  <div class="abs" style="left:820px;top:13px;font-size:7.5px;color:var(--muted)">Lena's Harvest Table © 2011 | Privacy Policy</div>
</div>
</body>
</html>
```